Real Estate Office Front Facade Redesign - ideas needed

Kindly read this brief thoroughly as there are 2 deliverables:
1. Office building façade redesign (see attached logo and also photo of our office building façade)
2. I also require a design for a freestanding signboard that will be coordinated with the design of the office front please see the images attached labelled signboard.

Deliverable number 1:
I am looking for a minimalist contemporary design with strong colours to draw the attention of the passing Traffic.

The office facade is to be repainted so you may choose to recolour the office in any way to coordinate with logo however the attached logo must remain as is. I prefer the colours red black and white or shades of these colours.

Vireo property managers is a new company looking to target property investors in the local area. Most of our clients are from a middle to upper income demographic. We help these investors to rent out their properties and ensure they are maintained in good condition and provide a regular income.

The area we operate in is centrally located and close to the central business district of Perth.

Our office is situated in a residential area on a busy road facing diagonally at 45° down the road. People see our office from their cars whilst driving to work, there is no pedestrian traffic in the area. Therefore the office façade needs to stand out and any signage must be read by quickly passing traffic or convey our brand in seconds. Whilst the view of the office from the road is obscured somewhat by trees from a distance, once within 50 to 100 m of the office the full face of the office front is visible facing directly at the driver.

No measurements are provided for the façade of the office (please see the photo provided), this is a blank canvas as the whole building will be repainted to fit in with YOUR design. A logo is also attached. The colours red black and white are preferred.

Please provide an image of the office with signage/colours superimposed.

Deliverable number 2:
Also attached is an image of a freestanding sign for which I require a design. This sign is used for advertising properties for lease or sale which will be erected outside the front of residential houses. Again this sign needs to be bold and bright with a contemporary design. It needs to stand out from the crowd of many other signs in the area, whilst the sign advertises the property it must also promote our company brand by having a prominent logo. The size of these signboards will either be 1250 mm x 900 mm or 1800 mm x 625 mm. Please note that this sign must be rectangular in shape and cannot have any text or logo protruding outside of the lines of the rectangular sign due to cost restrictions.

Target Market(s)

Industry/Entity Type

Real Estate

Font styles to use
Sans Serif

Colors
ec1f27
ffffff
000000

Requirements
Must have
• Contemporary uncluttered design using the colours red black and white of shades of.
Nice to have
• A prominent logo with the words "Property Managers" easily read by passing traffic.
• Files provided with editable text and the name of the font used.
Should not have
• designs protruding outside of the overall building facia or sign rectangle.

```html
<!DOCTYPE html>
<html lang="en">
<head>
<meta charset="utf-8">
<title>Vireo Property Managers – For Lease Signboard</title>
<link rel="stylesheet" href="https://fonts.googleapis.com/css2?family=Source+Sans+3:wght@300;400;600;700&display=swap">
<style>
  :root {
    --brand-red: #ec1f27;
    --brand-black: #000000;
    --brand-white: #ffffff;
    --backdrop: #e6e6e4;
    --sign-edge: #cfcfcf;
  }
  * { box-sizing: border-box; margin: 0; padding: 0; }
  html, body {
    width: 1200px;
    height: 763px;
    overflow: hidden;
    background: var(--backdrop);
    font-family: "Source Sans 3", sans-serif;
  }
  .signboard {
    position: absolute;
    left: 390px;
    top: 32px;
    width: 420px;
    height: 700px;
    overflow: hidden;
    background: var(--brand-white);
    box-shadow: 0 0 0 1px var(--sign-edge);
  }
  .signboard__shapes {
    position: absolute;
    inset: 0;
    width: 420px;
    height: 700px;
  }
  .brand {
    position: absolute;
    top: 40px;
    left: 168px;
    width: 220px;
    display: flex;
    flex-direction: column;
    align-items: center;
    color: var(--brand-black);
  }
  .brand__row {
    display: flex;
    align-items: center;
    gap: 10px;
  }
  .brand__mark {
    width: 22px;
    height: 22px;
    background: var(--brand-red);
  }
  .brand__name {
    font-weight: 300;
    font-size: 44px;
    letter-spacing: 4px;
    line-height: 1;
  }
  .brand__tagline {
    margin-top: 6px;
    font-weight: 300;
    font-size: 11px;
    letter-spacing: 2.5px;
  }
  .listing {
    position: absolute;
    left: 58px;
    top: 318px;
    color: var(--brand-white);
  }
  .listing__status {
    font-weight: 600;
    font-size: 52px;
    line-height: 1;
    letter-spacing: 0.5px;
  }
  .contact {
    list-style: none;
    margin-top: 22px;
  }
  .contact__item {
    display: flex;
    align-items: center;
    font-size: 16px;
    font-weight: 400;
    line-height: 1;
    height: 30px;
  }
  .contact__icon {
    width: 16px;
    height: 16px;
    margin-right: 8px;
  }
  .contact__divider {
    width: 1px;
    height: 18px;
    background: var(--brand-white);
    margin-right: 8px;
  }
</style>
</head>
<body>
  <main class="signboard">
    <svg class="signboard__shapes" viewBox="0 0 420 700" aria-hidden="true">
      <rect class="base-diamond" x="-20" y="470" width="470" height="470" rx="40"
            transform="rotate(45 215 705)" fill="var(--brand-black)"/>
      <rect class="feature-diamond" x="-5" y="195" width="380" height="380" rx="46"
            transform="rotate(45 185 385)" fill="var(--brand-red)"/>
    </svg>

    <header class="brand">
      <div class="brand__row">
        <span class="brand__mark"></span>
        <span class="brand__name">VIREO</span>
      </div>
      <span class="brand__tagline">PROPERTY MANAGERS</span>
    </header>

    <section class="listing">
      <h1 class="listing__status">FOR LEASE</h1>
      <ul class="contact">
        <li class="contact__item">
          <svg class="contact__icon" viewBox="0 0 16 16"><rect x="4" y="1" width="8" height="14" rx="1.5" fill="none" stroke="var(--brand-white)" stroke-width="1.4"/><circle cx="8" cy="12.5" r="0.9" fill="var(--brand-white)"/></svg>
          <span class="contact__divider"></span>Mob. 0400 123 456
        </li>
        <li class="contact__item">
          <svg class="contact__icon" viewBox="0 0 16 16"><path d="M3.5 1.5 L6 1.5 L7 5 L5.3 6.3 C6 8 8 10 9.7 10.7 L11 9 L14.5 10 L14.5 12.5 C14.5 13.6 13.6 14.5 12.5 14.5 C6.9 14.5 1.5 9.1 1.5 3.5 C1.5 2.4 2.4 1.5 3.5 1.5 Z" fill="var(--brand-white)"/></svg>
          <span class="contact__divider"></span>Office. 9400 7788
        </li>
        <li class="contact__item">
          <svg class="contact__icon" viewBox="0 0 16 16"><circle cx="8" cy="8" r="6.5" fill="none" stroke="var(--brand-white)" stroke-width="1.4"/><path d="M1.5 8 H14.5 M8 1.5 C5 5 5 11 8 14.5 M8 1.5 C11 5 11 11 8 14.5" fill="none" stroke="var(--brand-white)" stroke-width="1.1"/></svg>
          <span class="contact__divider"></span>www.vireoproperty.com.au
        </li>
      </ul>
    </section>
  </main>
</body>
</html>
```